2021 Summer Ads Whitmore Ash Custom Homes

We need a re-design of our summer ad run for our customer, Whitmore Ash Custom Homes. They are custom home builders in the mostly rural parts of West Virginia, USA. They are known for their "Forever Home" tagline. We'd like two designed ads with the main difference being just the custom home that's featured. These designs should be for a Google banner like 300 x 250 and square ad like 250 x 250. For inspiration please visit the Whitmore Ash Custom Homes website at www dot whitmoreashcustomhomes dot com

Target Market(s)

consumers / new home shoppers

Industry/Entity Type

Consumer

Requirements
Must have
• WACH logo
Price Lock Available!
Custom home pic
Learn more >
small QVTG logo mark

```html
<!DOCTYPE html>
<html lang="en">
<head>
<meta charset="utf-8">
<title>Whitmore Ash Custom Homes – Forever Home</title>
<link rel="stylesheet" href="https://fonts.googleapis.com/css2?family=Allura&family=Montserrat:wght@300;600;700&display=swap">
<style>
  :root{
    --charcoal:#333537;
    --brand-red:#9b1c20;
    --shadow-grey:#e7e7ea;
    --white:#ffffff;
    --guild-blue:#1d3f9a;
    --roof-grey:#6f7377;
  }
  html,body{margin:0;padding:0;overflow:hidden;background:var(--white);}
  .ad{position:relative;width:1199px;height:1200px;overflow:hidden;background:var(--white);font-family:'Montserrat',sans-serif;}
  .ad__shapes{position:absolute;inset:0;width:1199px;height:1200px;}
  .tagline-script{position:absolute;left:136px;top:100px;margin:0;font-family:'Allura',cursive;font-size:150px;line-height:1;color:var(--white);font-weight:400;}
  .tagline-main{position:absolute;left:112px;top:222px;margin:0;font-family:'Montserrat',sans-serif;font-weight:700;font-size:196px;line-height:1;letter-spacing:2px;color:var(--white);}
  .offer{position:absolute;left:110px;top:492px;margin:0;color:var(--white);font-size:48px;line-height:1.2;}
  .offer__light{display:block;font-weight:300;letter-spacing:1px;}
  .offer__bold{display:block;font-weight:600;letter-spacing:1px;}
  .cta{position:absolute;left:103px;top:672px;width:296px;height:79px;border-radius:18px;background:var(--brand-red);color:var(--white);font-weight:600;font-size:27px;letter-spacing:.5px;display:flex;align-items:center;justify-content:center;text-decoration:none;}
  .brand{position:absolute;left:820px;top:88px;width:340px;text-align:center;color:var(--brand-red);font-family:'Montserrat',sans-serif;font-weight:700;font-size:36px;line-height:1.15;}
  .brand__mark{display:block;width:34px;height:34px;margin:0 auto 12px;background:var(--brand-red);}
  .guild{position:absolute;left:1030px;top:1100px;width:140px;color:var(--guild-blue);font-weight:700;}
  .guild__name{display:flex;align-items:center;gap:8px;font-size:38px;line-height:1;}
  .guild__mark{width:22px;height:22px;background:var(--guild-blue);}
  .guild__full{margin-top:6px;font-size:13px;line-height:1.15;}
</style>
</head>
<body>
<main class="ad">
  <svg class="ad__shapes" viewBox="0 0 826 835" preserveAspectRatio="none" aria-hidden="false">
    <defs>
      <clipPath id="panel-clip">
        <path d="M0 0 H395 L630 235 Q655 260 630 285 L185 730 Q160 755 135 730 L0 595 Z"/>
      </clipPath>
      <linearGradient id="home-tones" x1="0" y1="0" x2="0" y2="1">
        <stop offset="0" stop-color="#dfe8ef"/>
        <stop offset=".12" stop-color="#4f7a34"/>
        <stop offset=".45" stop-color="#3f6a2a"/>
        <stop offset=".55" stop-color="#6f7377"/>
        <stop offset=".7" stop-color="#a2262a"/>
        <stop offset="1" stop-color="#8e1e22"/>
      </linearGradient>
    </defs>
    <path class="panel-shadow" fill="var(--shadow-grey)" d="M12 0 H407 L645 250 Q670 275 645 300 L200 748 Q175 773 150 748 L0 610 Z"/>
    <path class="panel" fill="var(--charcoal)" d="M0 0 H395 L630 235 Q655 260 630 285 L185 730 Q160 755 135 730 L0 595 Z"/>
    <rect class="panel-band" clip-path="url(#panel-clip)" x="0" y="148" width="700" height="152" fill="var(--brand-red)"/>
    <rect x="302" y="412" width="456" height="456" rx="46" fill="var(--shadow-grey)" transform="rotate(45 530 640)"/>
    <rect x="310" y="420" width="440" height="440" rx="42" fill="var(--white)" transform="rotate(45 530 630)"/>
    <rect role="img" aria-label="Photo of a red board-and-batten custom home with grey roof, cupola and attached garage, set against tall green trees" x="320" y="420" width="420" height="420" rx="38" fill="url(#home-tones)" transform="rotate(45 530 630)"/>
  </svg>

  <p class="tagline-script">Forever</p>
  <h1 class="tagline-main">HOME</h1>

  <p class="offer">
    <span class="offer__light">PRICE LOCK</span>
    <span class="offer__bold">AVAILABLE!</span>
  </p>

  <a class="cta" href="#">LEARN MORE</a>

  <div class="brand">
    <span class="brand__mark"></span>
    Whitmore Ash<br>Custom Homes
  </div>

  <div class="guild">
    <div class="guild__name"><span class="guild__mark"></span>QVTG</div>
    <div class="guild__full">Quarry Valley<br>Trade Guild</div>
  </div>
</main>
</body>
</html>
```